Visitenkarten-Design für Styling-Coach
Zielgruppe
Styling Coach
Aufgabenstellung
Colors, Logo, Two side design, one side with Information/Logo other backside nice design
Info Card Front:
Helene Sofia Krantz
Lindenhof 27
8847 Talberg
krantz@krantzstyling.example
www.krantzstyling.example

```html
<!DOCTYPE html>
<html lang="de">
<head>
<meta charset="utf-8">
<title>Helene Sofia Krantz – Visitenkarten</title>
<link rel="stylesheet" href="https://fonts.googleapis.com/css2?family=Kaushan+Script&family=Open+Sans:wght@300;400&display=swap">
<style>
  :root {
    --backdrop: #d5dae4;
    --pink-light: #f4bfd2;
    --pink-mid: #e286b3;
    --pink-deep: #d7358f;
    --pink-soft: #f7e3ec;
    --card-white: #f8f8f8;
    --ink: #1c1c1c;
    --label-pink: #e789b4;
    --logo-white: #ffffff;
  }
  * { margin: 0; padding: 0; box-sizing: border-box; }
  html, body {
    width: 1200px;
    height: 800px;
    overflow: hidden;
    background: var(--backdrop);
  }
  .canvas {
    position: relative;
    width: 1200px;
    height: 800px;
  }
  .card {
    position: absolute;
    left: 380px;
    width: 440px;
    height: 270px;
    overflow: hidden;
    box-shadow: 0 4px 10px rgba(40, 45, 60, 0.25);
  }

  /* Brand side */
  .card--brand {
    top: 100px;
    background: linear-gradient(100deg, var(--pink-light) 0%, var(--pink-mid) 55%, var(--pink-deep) 100%);
  }
  .brand-lockup {
    position: absolute;
    left: 0;
    right: 0;
    top: 100px;
    text-align: center;
    color: var(--logo-white);
    font-family: "Open Sans", sans-serif;
    font-weight: 300;
  }
  .brand-name {
    display: inline-flex;
    align-items: center;
    gap: 10px;
    font-size: 19px;
    letter-spacing: 1px;
  }
  .brand-dot {
    width: 10px;
    height: 10px;
    border-radius: 50%;
    background: var(--logo-white);
  }
  .brand-tagline {
    margin-top: 8px;
    font-size: 20px;
    letter-spacing: 9px;
  }

  /* Info side */
  .card--info {
    top: 410px;
    background: var(--card-white);
  }
  .info-accent {
    position: absolute;
    left: -90px;
    top: 60px;
    width: 240px;
    height: 240px;
    border-radius: 50%;
    background: linear-gradient(135deg, var(--pink-soft), var(--pink-mid));
    opacity: 0.85;
  }
  .info-block {
    position: absolute;
    left: 200px;
    top: 34px;
    color: var(--ink);
    font-family: "Open Sans", sans-serif;
    font-size: 13px;
    line-height: 1.35;
  }
  .info-name {
    font-family: "Kaushan Script", cursive;
    font-size: 20px;
    line-height: 1.1;
    white-space: nowrap;
  }
  .info-role {
    margin-top: 2px;
    font-size: 13px;
  }
  .info-address {
    margin-top: 14px;
  }
  .info-phones {
    margin-top: 12px;
  }
  .phone-label {
    display: inline-block;
    width: 22px;
    color: var(--label-pink);
    font-weight: 400;
  }
  .info-web {
    margin-top: 12px;
  }
</style>
</head>
<body>
<main class="canvas">

  <section class="card card--brand" aria-label="Kartenrückseite">
    <div class="brand-lockup">
      <div class="brand-name"><span class="brand-dot"></span>HELENE SOFIA KRANTZ</div>
      <div class="brand-tagline">STYLING COACH</div>
    </div>
  </section>

  <section class="card card--info" aria-label="Kartenvorderseite">
    <div class="info-accent" role="img" aria-label="Dekorative Fläche in Rosatönen"></div>
    <div class="info-block">
      <p class="info-name">Helene Sofia Krantz</p>
      <p class="info-role">Styling Coach</p>
      <p class="info-address">Lindenhof 27<br>8847 Talberg</p>
      <p class="info-phones">
        <span class="phone-label">T :</span>+41 44 555 0132<br>
        <span class="phone-label">F :</span>+41 79 555 0187
      </p>
      <p class="info-web">krantz@krantzstyling.example<br>www.krantzstyling.example</p>
    </div>
  </section>

</main>
</body>
</html>
```